Wedding Day Custom Wine Label - Tasmanian (Tamar Valley) wine

I am looking for a custom design that will be put on a wine label to commemorate a very good friend's wedding day.

We will need to be able to take the design and print it on to sticker labels that we can put on to wine bottles.

The bride and groom have asked for a simplistic label design (see example image attached). We need two labels. One for "Pinot Noir" wine and the other for "Chardonnay" wine. We would like the label to say:

The Drumwell's
Pinot Noir
2023
Tamar Valley

and for for the other wine variety:

The Drumwell's
Chardonnay
2023
Tamar Valley

smaller text below to say:

13.5% ALC/VOL 750ML
MAREN & JONAS - 31.10.2024

I am happy to consider other variations - the bride & groom would prefer something minimalistic. Elegant and classy.

Target Market(s)

the bride & groom

Requirements
Must have
• Wedding date (31.10.2024). Wine type (Pinot Noir or Chardonnay).
Should not have
• images not essential

```html
<!DOCTYPE html>
<html lang="en">
<head>
<meta charset="UTF-8">
<title>The Drumwell's Wedding Wine Labels</title>
<link rel="stylesheet" href="https://fonts.googleapis.com/css2?family=Cinzel:wght@400;500&family=Libre+Baskerville:wght@700&family=Montserrat:wght@400;500&display=swap">
<style>
  :root {
    --backdrop: #ececec;
    --label-white: #f7f7f6;
    --gold: #9a7a17;
    --gold-deep: #7d6210;
    --gold-light: #b8952c;
    --ink: #1c1c1c;
  }
  * { box-sizing: border-box; margin: 0; padding: 0; }
  html, body {
    width: 1000px;
    height: 1200px;
    overflow: hidden;
    background: var(--backdrop);
  }
  .label-sheet {
    width: 1000px;
    height: 1200px;
    display: flex;
    justify-content: center;
    align-items: center;
    gap: 50px;
  }
  .wine-label {
    position: relative;
    width: 420px;
    height: 640px;
    background: var(--label-white);
    box-shadow: 0 2px 10px rgba(0,0,0,0.08);
    display: flex;
    flex-direction: column;
    align-items: center;
  }
  .wine-label::before {
    content: "";
    position: absolute;
    inset: 12px;
    border: 1.5px solid var(--gold);
    pointer-events: none;
  }
  .ornament {
    display: block;
    background: linear-gradient(180deg, var(--gold-light), var(--gold-deep));
    border-radius: 4px;
  }
  .ornament--crest {
    width: 56px;
    height: 40px;
    margin-top: 62px;
  }
  .name-banner {
    margin-top: 8px;
    display: flex;
    align-items: center;
    width: 356px;
  }
  .name-banner__rule {
    flex: 1;
    height: 2px;
    background: var(--gold);
  }
  .name-banner__plate {
    background: linear-gradient(180deg, var(--gold-light), var(--gold) 50%, var(--gold-deep));
    border-radius: 6px;
    padding: 9px 22px 7px;
    font-family: "Cinzel", serif;
    font-weight: 400;
    font-size: 27px;
    letter-spacing: 0.5px;
    color: var(--label-white);
    white-space: nowrap;
  }
  .wine-variety {
    margin-top: 66px;
    font-family: "Cinzel", serif;
    font-weight: 400;
    font-size: 45px;
    color: var(--ink);
    letter-spacing: 0.5px;
    white-space: nowrap;
  }
  .wine-region {
    margin-top: 42px;
    font-family: "Libre Baskerville", serif;
    font-weight: 700;
    font-size: 23px;
    color: var(--gold);
  }
  .wine-vintage {
    margin-top: 18px;
    font-family: "Libre Baskerville", serif;
    font-weight: 700;
    font-size: 24px;
    color: var(--gold);
  }
  .ornament--flourish {
    width: 190px;
    height: 34px;
    margin-top: 34px;
  }
  .label-details {
    margin-top: auto;
    margin-bottom: 42px;
    text-align: center;
    font-family: "Montserrat", sans-serif;
    font-size: 13px;
    line-height: 1.35;
  }
  .label-details__volume { color: var(--ink); }
  .label-details__dedication { color: var(--gold); }
</style>
</head>
<body>
  <main class="label-sheet">
    <article class="wine-label wine-label--pinot">
      <span class="ornament ornament--crest" role="img" aria-label="Gold filigree crest ornament"></span>
      <div class="name-banner">
        <span class="name-banner__rule"></span>
        <span class="name-banner__plate">THE DRUMWELL'S</span>
        <span class="name-banner__rule"></span>
      </div>
      <h1 class="wine-variety">PINOT NOIR</h1>
      <p class="wine-region">TAMAR VALLEY</p>
      <p class="wine-vintage">2023</p>
      <span class="ornament ornament--flourish" role="img" aria-label="Gold scroll flourish divider"></span>
      <footer class="label-details">
        <p class="label-details__volume">13.5% ALC/VOL 750ML</p>
        <p class="label-details__dedication">MAREN &amp; JONAS - 31.10.2024</p>
      </footer>
    </article>

    <article class="wine-label wine-label--chardonnay">
      <span class="ornament ornament--crest" role="img" aria-label="Gold filigree crest ornament"></span>
      <div class="name-banner">
        <span class="name-banner__rule"></span>
        <span class="name-banner__plate">THE DRUMWELL'S</span>
        <span class="name-banner__rule"></span>
      </div>
      <h1 class="wine-variety">CHARDONNAY</h1>
      <p class="wine-region">TAMAR VALLEY</p>
      <p class="wine-vintage">2023</p>
      <span class="ornament ornament--flourish" role="img" aria-label="Gold scroll flourish divider"></span>
      <footer class="label-details">
        <p class="label-details__volume">13.5% ALC/VOL 750ML</p>
        <p class="label-details__dedication">MAREN &amp; JONAS - 31.10.2024</p>
      </footer>
    </article>
  </main>
</body>
</html>
```